NEW YORK Plumbing/utility company 10 year anniversary business card

Looking For simple back and front business card would like to include a few things in description
We offer 24/7 emergency service
residential
commercial
industrial
municipal
services offered
Plumbing
hydro excavation
hydro jetting
Well pumps
Sewer pumps
water mains
sewer mains

```html
<!DOCTYPE html>
<html lang="en">
<head>
<meta charset="utf-8">
<title>Ridgeline Water &amp; Sewer – Business Card</title>
<link href="https://fonts.googleapis.com/css2?family=Montserrat:wght@400;500;600;700;800&display=swap" rel="stylesheet">
<style>
  :root{
    --blue:#0866a6;
    --sky:#11a4e8;
    --red:#e8141c;
    --grey:#8a8a8a;
    --white:#ffffff;
    --bg:#2a2a2a;
  }
  *{box-sizing:border-box;margin:0;padding:0}
  html,body{width:1200px;height:1024px;overflow:hidden;background:var(--bg);font-family:"Montserrat",sans-serif}
  .card{position:absolute;left:220px;width:760px;height:434px;background:var(--white);overflow:hidden;box-shadow:0 10px 30px rgba(0,0,0,.45)}
  .card--front{top:48px}
  .card--back{top:542px}
  .band{position:absolute;left:0;right:0;bottom:0;background:var(--blue)}
  .card--front .band{height:190px}
  .card--back .band{height:168px}

  .brand{position:absolute;left:0;right:0;display:flex;align-items:center;justify-content:center;gap:16px;white-space:nowrap}
  .brand__dot{width:34px;height:34px;border-radius:50%;background:var(--sky);flex:none}
  .brand__name{font-weight:800;color:var(--grey);letter-spacing:2px;line-height:1}
  .card--front .brand{top:42px}
  .card--front .brand__name{font-size:64px}

  .headline{position:absolute;top:128px;left:0;right:0;text-align:center;color:var(--red);font-weight:800;font-size:30px;letter-spacing:.5px;white-space:nowrap}
  .rule{position:absolute;top:177px;left:150px;right:150px;height:2px;background:linear-gradient(90deg,transparent,var(--grey) 20%,var(--grey) 80%,transparent)}
  .rule::after{content:"";position:absolute;left:50%;top:-4px;width:10px;height:10px;margin-left:-5px;border-radius:50%;background:var(--white);border:2px solid var(--grey)}
  .sectors{position:absolute;top:196px;left:0;right:0;display:flex;justify-content:center;gap:16px;font-weight:800;font-size:19px;color:var(--sky);letter-spacing:.3px;white-space:nowrap}
  .sectors .sep{color:var(--red);font-weight:400}
  .pill{position:absolute;top:228px;left:50%;transform:translateX(-50%);background:var(--red);color:var(--white);font-weight:800;font-size:20px;padding:8px 26px;border-radius:22px;border:3px solid var(--white);white-space:nowrap}
  .services{position:absolute;top:296px;left:0;right:0;text-align:center;color:var(--white);font-size:21px;line-height:1.55;font-weight:400}
  .services .dot{color:var(--sky);margin:0 8px}

  .panel{position:absolute;left:130px;width:500px;top:0;height:330px;background:var(--white);border-radius:0 0 16px 16px}
  .card--back .brand{top:110px}
  .card--back .brand__name{font-size:68px}
  .tagline{position:absolute;top:220px;left:0;right:0;display:flex;align-items:center;justify-content:center;gap:16px;color:var(--sky);font-weight:700;font-size:28px;letter-spacing:6px;white-space:nowrap}
  .tagline::before,.tagline::after{content:"";width:56px;height:3px;background:var(--sky)}
  .contact{position:absolute;bottom:40px;left:0;right:0;display:flex;justify-content:center;align-items:center;gap:30px;color:var(--white);font-size:26px;font-weight:500;white-space:nowrap}
  .contact__item{display:flex;align-items:center;gap:10px}
  .icon{width:32px;height:32px;border-radius:8px;background:var(--red);display:inline-flex;align-items:center;justify-content:center;flex:none}
</style>
</head>
<body>
  <section class="card card--front">
    <div class="band"></div>
    <div class="brand"><span class="brand__dot"></span><span class="brand__name">RIDGELINE</span></div>
    <p class="headline">WE OFFER 24/7 EMERGENCY SERVICE</p>
    <div class="rule"></div>
    <p class="sectors"><span>RESIDENTIAL</span><span class="sep">|</span><span>COMMERCIAL</span><span class="sep">|</span><span>INDUSTRIAL</span><span class="sep">|</span><span>MUNICIPAL</span></p>
    <p class="pill">SERVICES OFFERED</p>
    <p class="services">
      Plumbing<span class="dot">•</span>Hydro Excavation<span class="dot">•</span>Hydro Jetting<span class="dot">•</span>Well Pumps<br>
      Sewer Pumps<span class="dot">•</span>Water Mains<span class="dot">•</span>Sewer Mains
    </p>
  </section>

  <section class="card card--back">
    <div class="band"></div>
    <div class="panel">
      <div class="brand"><span class="brand__dot"></span><span class="brand__name">RIDGELINE</span></div>
      <p class="tagline">WATER &amp; SEWER</p>
    </div>
    <div class="contact">
      <span class="contact__item">
        <span class="icon"><svg width="18" height="18" viewBox="0 0 24 24"><path fill="#fff" d="M6.6 10.8a15 15 0 0 0 6.6 6.6l2.2-2.2a1 1 0 0 1 1-.25 11.4 11.4 0 0 0 3.6.57 1 1 0 0 1 1 1V20a1 1 0 0 1-1 1A17 17 0 0 1 3 4a1 1 0 0 1 1-1h3.5a1 1 0 0 1 1 1c0 1.25.2 2.45.57 3.57a1 1 0 0 1-.25 1z"/></svg></span>
        845-555-0132
      </span>
      <span class="contact__item">
        <span class="icon"><svg width="18" height="18" viewBox="0 0 24 24"><rect x="3" y="5" width="18" height="14" rx="2" fill="none" stroke="#fff" stroke-width="2"/><path d="M3 7l9 6 9-6" fill="none" stroke="#fff" stroke-width="2"/></svg></span>
        info@ridgelinewater.com
      </span>
    </div>
  </section>
</body>
</html>
```